Banner for back of trucks

We make a product that is called "Brindo".
It attaches to the side of hay balers and automatically applies tags to bales as they are being made.
We require a simple / modern banner design that will be affixed to the back of hay trucks showing that the hay on board has been Marked by Brindo.
The banner will be 52x91cm (landscape)
The banner needs to say "Marked by Brindo" using the company logo.
It also needs the website "www.brindo.com.au" displayed.
We have attached an image of our logo, the product itself and the back of a truck it will be attached to for reference.

```html
<!DOCTYPE html>
<html lang="en">
<head>
<meta charset="utf-8">
<title>Marked by Brindo – Truck Banner</title>
<link rel="stylesheet" href="https://fonts.googleapis.com/css2?family=Montserrat:wght@500;600;800&display=swap">
<style>
  :root {
    --brown: #5a4738;
    --orange: #feae33;
    --white: #ffffff;
    --backdrop: #f4f4f4;
  }
  * { margin: 0; padding: 0; box-sizing: border-box; }
  html, body {
    width: 1200px;
    height: 1200px;
    overflow: hidden;
    background: var(--backdrop);
    font-family: "Montserrat", Arial, sans-serif;
  }
  .banner {
    position: absolute;
    left: 0;
    top: 257px;
    width: 1200px;
    height: 686px;
    background: var(--brown);
  }
  .banner__tagline {
    position: absolute;
    left: 0;
    right: 0;
    top: 105px;
    text-align: center;
    color: var(--white);
    font-weight: 500;
    font-size: 124px;
    line-height: 1;
    letter-spacing: 1px;
  }
  .banner__band {
    position: absolute;
    left: 0;
    top: 256px;
    width: 100%;
    height: 229px;
    background: var(--orange);
    display: flex;
    align-items: center;
    justify-content: center;
  }
  .banner__brand {
    color: var(--brown);
    font-weight: 800;
    font-size: 190px;
    line-height: 1;
    letter-spacing: 2px;
    margin-top: -8px;
  }
  .banner__web {
    position: absolute;
    left: 0;
    top: 568px;
    width: 100%;
    display: flex;
    align-items: center;
    gap: 26px;
  }
  .banner__rule {
    flex: 1;
    height: 8px;
    background: var(--white);
  }
  .banner__url {
    color: var(--white);
    font-weight: 600;
    font-size: 60px;
    line-height: 1;
    letter-spacing: 5px;
    white-space: nowrap;
  }
</style>
</head>
<body>
  <section class="banner">
    <h1 class="banner__tagline">Marked by</h1>
    <div class="banner__band">
      <span class="banner__brand">Brindo</span>
    </div>
    <div class="banner__web">
      <span class="banner__rule"></span>
      <span class="banner__url">www.brindo.com.au</span>
      <span class="banner__rule"></span>
    </div>
  </section>
</body>
</html>
```